Kitchen and cabinet shop needs new website

Dunmore Cabinets is a mid-sized, family run cabinet shop that is in the process of updating it's image after being handed over to the second generation. It's been in the business for almost 30 years and our designers have lots of experience in the design, home building and renovation industry. Our business offers free home consultations or a customer can visit our showroom to start the design process. Whether the client is a designer, home builder or homeowner we can help create the kitchen and space you're after by helping every step of the way.

The website needs to showcase our past work, (pictures to be included), show the different styles (eg. traditional, modern) and different areas of the home we can produce cabinets for. We created a new logo with Logo forge that needs to be included in the website as well as the colours. I would like 5 pages;
-Home page
-About us
-portfolio/gallery
-services
-contact us

I would like the website to have a contemporary look, nothing too busy or complicated.

I will attach some pictures with the different styles of our work I mentioned above and provide content for each job.

Target Market(s)

home owners, designer, home builders, business owners

Industry/Entity Type

Home Builder

Number of Pages Required

5+ page

Font styles to use
Sans Serif

Requirements
Must have
• home page, about us page, gallery/portfolio page-showing various pictures of our work and different styles, services page and contact us.
• Use logo and similar colours as in logo for the scheme
• more content and pictures to follow...

```html
<!DOCTYPE html>
<html lang="en">
<head>
<meta charset="utf-8">
<title>Contact Us – Dunmore Cabinets</title>
<link rel="stylesheet" href="https://fonts.googleapis.com/css2?family=Arimo:wght@400;700&family=Noto+Sans:wght@400&display=swap">
<style>
  :root {
    --orange: #f47920;
    --sky: #b3c1fb;
    --footer-blue: #3f6dc8;
    --brand-blue: #1f64b4;
    --white: #ffffff;
    --ink: #000000;
    --navy-ink: #000033;
    --quote-grey: #adadad;
    --button-blue: #1e90ff;
    --nav-active: #e3e6ff;
    --footer-text: #e6eaff;
  }
  * { box-sizing: border-box; margin: 0; padding: 0; }
  html, body { width: 1200px; height: 900px; overflow: hidden; }
  body {
    position: relative;
    background: linear-gradient(to bottom, var(--white) 0 150px, var(--sky) 150px 800px, var(--footer-blue) 800px);
    font-family: "Noto Sans", sans-serif;
    color: var(--ink);
  }
  .top-bar { position: absolute; left: 99px; top: 0; width: 1002px; height: 15px; background: var(--orange); }
  .brand {
    position: absolute; left: 108px; top: 42px;
    display: flex; align-items: center; gap: 12px;
    font-family: "Arimo", sans-serif; font-weight: 700; font-size: 34px;
    color: var(--brand-blue); letter-spacing: 1px;
  }
  .brand-square { width: 40px; height: 40px; background: var(--brand-blue); }
  .main-nav { position: absolute; left: 100px; top: 116px; width: 1001px; height: 34px; background: var(--orange); }
  .main-nav a {
    position: absolute; top: 9px;
    font-family: "Arimo", sans-serif; font-weight: 700; font-size: 14px;
    color: var(--white); text-decoration: none;
  }
  .main-nav a.active { color: var(--nav-active); }
  .main-nav .divider { position: absolute; top: 8px; width: 3px; height: 16px; background: var(--white); }
  .content-panel { position: absolute; left: 96px; top: 156px; width: 700px; height: 622px; background: var(--white); }
  .page-title {
    position: absolute; left: 11px; top: 18px;
    font-family: "Arimo", sans-serif; font-weight: 700; font-size: 27px;
  }
  .address { position: absolute; left: 14px; top: 74px; font-size: 18px; line-height: 22px; font-style: normal; }
  .contact-form label { position: absolute; left: 14px; font-size: 18px; }
  .contact-form .field { position: absolute; border: 3px solid var(--ink); background: var(--white); }
  .submit-button {
    position: absolute; left: 231px; top: 462px; width: 66px; height: 23px;
    background: var(--button-blue); border: 2px solid; border-color: #6ab8ff #00306a #00306a #6ab8ff;
    font-family: "Noto Sans", sans-serif; font-size: 16px; color: var(--ink);
  }
  .sidebar { position: absolute; left: 801px; top: 158px; width: 300px; height: 621px; background: var(--white); }
  .search-box {
    position: absolute; left: 12px; top: 6px; width: 88px; height: 15px;
    border: 1px solid #555; font-size: 8px; padding: 2px 0 0 3px; color: #333;
  }
  .sidebar-title { position: absolute; left: 6px; top: 34px; font-family: "Arimo", sans-serif; font-weight: 700; font-size: 16px; }
  .testimonial { position: absolute; right: 2px; color: var(--navy-ink); font-size: 14px; line-height: 16px; }
  .testimonial blockquote { background: var(--quote-grey); padding: 1px 2px; }
  .testimonial cite { display: block; text-align: right; font-style: normal; margin-top: 4px; padding-right: 4px; }
  .site-footer {
    position: absolute; left: 755px; top: 813px;
    font-family: "Arimo", sans-serif; font-size: 14px; line-height: 16px; color: var(--footer-text);
  }
</style>
</head>
<body>
  <div class="top-bar"></div>
  <header class="brand"><span class="brand-square"></span>DUNMORE CABINETS</header>

  <nav class="main-nav">
    <a class="active" style="left:8px">Home</a>
    <span class="divider" style="left:63px"></span>
    <a style="left:78px">About</a>
    <span class="divider" style="left:134px"></span>
    <a style="left:147px">Gallery</a>
    <span class="divider" style="left:207px"></span>
    <a style="left:221px">Services</a>
    <span class="divider" style="left:294px"></span>
    <a style="left:308px">Testimonials</a>
    <span class="divider" style="left:406px"></span>
    <a style="left:423px; top:12px">Contact Us</a>
  </nav>

  <main class="content-panel">
    <h1 class="page-title">Contact Us</h1>
    <address class="address">
      Dunmore Cabinets Ltd.<br>
      1234 Mystreet<br>
      Mycity<br>
      Phone: (123)456-7890<br>
      email: myname@mydomain.com
    </address>
    <form class="contact-form">
      <label style="top:208px">Name:</label>
      <div class="field" style="left:76px; top:209px; width:220px; height:23px"></div>
      <label style="top:251px">Email:</label>
      <div class="field" style="left:76px; top:248px; width:220px; height:28px"></div>
      <label style="top:296px">Message:</label>
      <div class="field" style="left:16px; top:321px; width:280px; height:122px"></div>
      <button class="submit-button" type="button">Submit</button>
    </form>
  </main>

  <aside class="sidebar">
    <div class="search-box">Looking For</div>
    <h2 class="sidebar-title">Testimonials</h2>
    <figure class="testimonial" style="top:61px; left:7px">
      <blockquote>The cabinets Dunmore made were absolutely amazing! Working with them was a dream, their staff were all so professional and friendly. I would recommend them to anyone.</blockquote>
      <cite>John Doe</cite>
    </figure>
    <figure class="testimonial" style="top:181px; left:5px; right:1px">
      <blockquote>I'm just loving thier work, it's exactly what I was looking for! The cabinets fit the design of my kitchen perfectly!</blockquote>
      <cite style="padding-right:0">Jane Person</cite>
    </figure>
  </aside>

  <footer class="site-footer">(c) 2015 Dunmore Custom Cabinets Ltd, All rights reserved.</footer>
</body>
</html>
```